Corvane Supplies Business Card

Professional business card that stand out to our potential customers. Front and back with clean modern design

Industry/Entity Type

Oil and gas

Contact Information for Business Card

Name, address, website , office phone and cell number

Requirements
Must have
• Editable files for each employee

```html
<!DOCTYPE html>
<html lang="en">
<head>
<meta charset="utf-8">
<title>Corvane Supplies Business Card</title>
<link href="https://fonts.googleapis.com/css2?family=Poppins:wght@400;500;700;800&display=swap" rel="stylesheet">
<style>
  :root {
    --page-bg: #e9e9eb;
    --card-black: #1b1b1d;
    --card-black-text: #3a3a3d;
    --card-white: #ffffff;
    --brand-red: #e31e25;
    --brand-blue: #0aa9cc;
    --ink: #1d1d1f;
    --rule: #2a2a2a;
  }
  * { margin: 0; padding: 0; box-sizing: border-box; }
  html, body { width: 1200px; height: 900px; overflow: hidden; }
  body {
    background: var(--page-bg);
    font-family: "Poppins", Arial, sans-serif;
    position: relative;
  }
  .card {
    position: absolute;
    left: 320px;
    width: 560px;
    height: 320px;
    border-radius: 22px;
    overflow: hidden;
  }
  /* Back side */
  .card-back {
    top: 100px;
    background: var(--card-black);
    display: flex;
    align-items: center;
    justify-content: center;
    gap: 16px;
  }
  .card-back .brand-mark {
    width: 30px; height: 30px;
    background: var(--card-black-text);
  }
  .card-back .brand-name {
    font-weight: 700;
    font-size: 34px;
    letter-spacing: 1px;
    text-transform: uppercase;
    color: var(--card-black-text);
  }
  /* Front side */
  .card-front {
    top: 480px;
    background: var(--card-white);
    box-shadow: 0 2px 10px rgba(0,0,0,0.08);
  }
  .front-brand {
    position: absolute;
    left: 40px; top: 44px;
    display: flex; align-items: center; gap: 14px;
  }
  .front-brand .brand-mark {
    width: 30px; height: 30px;
    background: var(--brand-red);
  }
  .front-brand .brand-name {
    font-weight: 800;
    font-size: 32px;
    letter-spacing: 1px;
    text-transform: uppercase;
    color: var(--brand-red);
  }
  .person {
    position: absolute;
    right: 300px; top: 140px;
    text-align: right;
    color: var(--ink);
  }
  .person-name {
    font-weight: 700;
    font-size: 24px;
    color: var(--brand-red);
    line-height: 1.1;
  }
  .person-title { font-size: 13px; margin-bottom: 4px; }
  .person-address { font-size: 13px; line-height: 1.35; }
  .divider {
    position: absolute;
    left: 276px; top: 172px;
    width: 1.5px; height: 72px;
    background: var(--rule);
  }
  .contact-list {
    position: absolute;
    left: 292px; top: 170px;
    list-style: none;
    font-size: 13px;
    color: var(--ink);
    line-height: 1.4;
  }
  .contact-list li { display: flex; align-items: center; gap: 8px; }
  .contact-list svg { width: 11px; height: 11px; fill: var(--brand-red); flex: none; }
  .bottom-bands {
    position: absolute;
    left: 0; bottom: 0;
    width: 560px; height: 20px;
  }
</style>
</head>
<body>
  <section class="card card-back" aria-label="Card back">
    <span class="brand-mark"></span>
    <span class="brand-name">Corvane Supplies</span>
  </section>

  <section class="card card-front" aria-label="Card front">
    <div class="front-brand">
      <span class="brand-mark"></span>
      <span class="brand-name">Corvane Supplies</span>
    </div>

    <div class="person">
      <p class="person-name">Marcus Hale</p>
      <p class="person-title">President</p>
      <p class="person-address">412 N.Larkfield Suite 5<br>Midland, Tx 79701</p>
    </div>

    <div class="divider"></div>

    <ul class="contact-list">
      <li>
        <svg viewBox="0 0 24 24"><path d="M6.6 10.8a15 15 0 0 0 6.6 6.6l2.2-2.2c.3-.3.7-.4 1-.2 1.1.4 2.3.6 3.6.6.6 0 1 .4 1 1V20c0 .6-.4 1-1 1A17 17 0 0 1 3 4c0-.6.4-1 1-1h3.5c.6 0 1 .4 1 1 0 1.3.2 2.5.6 3.6.1.3 0 .7-.2 1z"/></svg>
        (555)214-0387
      </li>
      <li>
        <svg viewBox="0 0 24 24"><path d="M7 1h10a2 2 0 0 1 2 2v18a2 2 0 0 1-2 2H7a2 2 0 0 1-2-2V3a2 2 0 0 1 2-2zm0 3v14h10V4zm5 15.5a1 1 0 1 0 0 2 1 1 0 0 0 0-2z"/></svg>
        (555)214-0387
      </li>
      <li>
        <svg viewBox="0 0 24 24"><path d="M2 5h20v14H2zm2 2v.5l8 5 8-5V7z"/></svg>
        sales@corvanesupplies.com
      </li>
      <li>
        <svg viewBox="0 0 24 24"><circle cx="12" cy="12" r="10"/></svg>
        www.corvanesupplies.com
      </li>
    </ul>

    <svg class="bottom-bands" viewBox="0 0 560 20" preserveAspectRatio="none" aria-hidden="true">
      <polygon points="0,0 250,0 240,20 0,20" fill="var(--brand-red)"/>
      <polygon points="254,0 560,0 560,20 244,20" fill="var(--brand-blue)"/>
    </svg>
  </section>
</body>
</html>
```